Card for Real Estate Developer

We need a business card design for a Real Estate Development company based in Texas. We focus on retail, apartment and residential development. Our target is predominantly investors looking to us to place their money properly to achieve a significant return. On the other side we sell our services to large retailers as their preferred developer assisting them in locating, building and leasing their real estate.

Target Market(s)

Investors

Industry/Entity Type

Real Estate Development

Contact Information for Business Card

Would like to stay within the company color scheme, while keeping the design moderately simple.

Font styles to use
Other font styles liked:
• per attached document

Requirements
Must have
• Name
• Phone
• Email
• Website
• Logo Prominently Displayed
• Stay within the colors provided in the attached document

```html
<!DOCTYPE html>
<html lang="en">
<head>
<meta charset="utf-8">
<title>Brenhold Development – Business Card</title>
<link rel="stylesheet" href="https://fonts.googleapis.com/css2?family=Arimo:wght@400&family=Tinos:wght@400&display=swap">
<style>
  :root {
    --backdrop: #1f1f1f;
    --card: #efefef;
    --ink: #111111;
    --brand-ink: #3a3a3a;
    --brand-blue: #2ea6dc;
    --rule: #222222;
    --contact: #2a2a2a;
  }
  * { margin: 0; padding: 0; box-sizing: border-box; }
  html, body {
    width: 1200px; height: 800px; overflow: hidden;
    background: var(--backdrop);
  }
  .canvas { position: relative; width: 1200px; height: 800px; }
  .card {
    position: absolute; top: 238px;
    width: 536px; height: 306px;
    background: var(--card);
    overflow: hidden;
  }
  .card--front { left: 49px; }
  .card--back { left: 617px; }

  .brand { position: absolute; display: flex; align-items: center; gap: 12px; }
  .brand__mark { width: 22px; height: 22px; background: var(--brand-blue); flex: none; }
  .brand__name {
    font-family: "Tinos", serif; font-weight: 400;
    color: var(--brand-ink); line-height: 1.05;
    text-transform: uppercase; letter-spacing: 0.04em;
  }
  .card--front .brand { left: 24px; top: 118px; }
  .card--front .brand__name { font-size: 26px; }
  .card--back .brand { right: 30px; bottom: 28px; }
  .card--back .brand__name { font-size: 34px; text-align: right; }

  .holder { position: absolute; right: 21px; top: 160px; text-align: right; }
  .holder__name { font-family: "Tinos", serif; font-size: 33px; color: var(--ink); line-height: 1; }
  .holder__role { font-family: "Arimo", sans-serif; font-size: 17px; color: var(--ink); margin-top: 4px; }

  .divider {
    position: absolute; left: 0; top: 205px;
    width: 429px; height: 1px; background: var(--rule);
  }

  .contacts { position: absolute; left: 22px; top: 222px; list-style: none; }
  .contacts li {
    display: flex; align-items: center; gap: 12px;
    height: 23px; margin-bottom: 1px;
    font-family: "Arimo", sans-serif; font-size: 15px; color: var(--contact);
  }
  .contacts svg { width: 12px; height: 12px; flex: none; }
</style>
</head>
<body>
<div class="canvas">

  <section class="card card--front">
    <div class="brand">
      <span class="brand__mark"></span>
      <span class="brand__name">Brenhold<br>Development</span>
    </div>

    <div class="holder">
      <div class="holder__name">Ellis Harrow</div>
      <div class="holder__role">Manager</div>
    </div>

    <div class="divider"></div>

    <ul class="contacts">
      <li>
        <svg viewBox="0 0 12 12" aria-hidden="true"><rect width="12" height="12" fill="#2ea6dc"/><path d="M3.5 2.5 5 4 4.3 5.2a5 5 0 0 0 2.5 2.5L8 7l1.5 1.5-1 1C5.5 9.5 2.5 6.5 2.5 3.5z" fill="#fff"/></svg>
        02 5550 1847
      </li>
      <li>
        <svg viewBox="0 0 12 12" aria-hidden="true"><rect width="12" height="12" fill="#2ea6dc"/><rect x="2.5" y="3.5" width="7" height="5" fill="#fff"/><path d="M2.5 3.5 6 6.5 9.5 3.5" fill="none" stroke="#2ea6dc" stroke-width="0.8"/></svg>
        hello@brenholddev.com
      </li>
      <li>
        <svg viewBox="0 0 12 12" aria-hidden="true"><rect width="12" height="12" fill="#2ea6dc"/><circle cx="6" cy="6" r="3.5" fill="none" stroke="#fff" stroke-width="1"/><path d="M2.5 6h7M6 2.5v7" stroke="#fff" stroke-width="0.8"/></svg>
        www.brenholddevelopment.com
      </li>
    </ul>
  </section>

  <section class="card card--back">
    <div class="brand">
      <span class="brand__mark"></span>
      <span class="brand__name">Brenhold<br>Development</span>
    </div>
  </section>

</div>
</body>
</html>
```